Our soon to be released website will provide information on any drink and eat deals or other "themed" (recurring) events worth mentioning.
Visitors will be able to find the place they are looking for using tags, location,prices, timings and services.
Examples are: Ladies Night, Brunches, Happy Hour, Iftar, Business Lunch, Hotelier Night, etc.
Launching city = Dubai

Target Market(s)

Visitors of bars, clubs, lounges and restaurants in Dubai

Industry/Entity Type

Events

Contact Information for Business Card

Velvet Evenings and Feasts Dubai
Gustav ter Brolle
Founder
T +971 (0)50 - 314 2087
E gustav@VvelvetEveningsandFeastsDubai.example
I www.VelvetEveningsandFeastsDubai.example
Facebook /velveteveningsandfeastsdubai
Instagram /velvetevenings_feasts_dubai/
P.O. Box 487260, Dubai, United Arab Emirates (or) UAE
100% Velvet Evenings & Feasts
100% Up-to-date
100% Searchable

Logo Text

Velvet Evenings & Feasts (not the word Dubai)

Requirements
Must have
• Business cards should make clear that our company:
• - can attract more visitors for clubs, restaurants, bars etc.
Nice to have
• The website name will be: www.velveteveningsandfeastsdubai.example
• (and that's also the name of this project).
• We purely decided for this name so everybody knows what we offer (up to date and extensive infromation about recurring drink and eat deals) and it should help us as well in SEO.

```html
<!DOCTYPE html>
<html lang="en">
<head>
<meta charset="utf-8">
<title>Velvet Evenings &amp; Feasts Dubai — Business Card</title>
<link rel="stylesheet" href="https://fonts.googleapis.com/css2?family=Questrial&family=Roboto:wght@500;700&display=swap">
<style>
  :root {
    --page: #e6e6e6;
    --card: #fbfbfb;
    --card-shade: #ececec;
    --band: #555555;
    --band-text: #f2f2f2;
    --ink: #1a1a1a;
    --muted: #7a7a7a;
    --accent: #e3222b;
  }
  * { box-sizing: border-box; margin: 0; padding: 0; }
  html, body { width: 1200px; height: 1000px; overflow: hidden; }
  body {
    background: var(--page);
    font-family: "Questrial", sans-serif;
    color: var(--ink);
    position: relative;
  }
  .card {
    position: absolute;
    width: 540px;
    height: 310px;
    border-radius: 18px;
    overflow: hidden;
    background: radial-gradient(ellipse at 40% 35%, var(--card) 40%, var(--card-shade) 100%);
    box-shadow: 0 10px 30px rgba(0,0,0,0.18);
  }
  .card--front { left: 40px; top: 170px; }
  .card--back { left: 620px; top: 440px; }

  .brand-name {
    font-family: "Roboto", sans-serif;
    font-weight: 700;
    color: var(--ink);
    line-height: 1.05;
    text-align: center;
  }
  .card--front .brand {
    position: absolute; left: 0; right: 0; top: 70px;
    text-align: center;
  }
  .card--front .brand-name { font-size: 34px; letter-spacing: 3px; }
  .brand-tagline {
    font-family: "Questrial", sans-serif;
    letter-spacing: 6px;
    color: var(--ink);
    margin-top: 10px;
  }
  .card--front .brand-tagline { font-size: 15px; }

  .social-band {
    position: absolute; left: 0; right: 0; bottom: 0;
    height: 72px;
    background: var(--band);
    display: flex; align-items: center; justify-content: space-between;
    padding: 0 28px;
  }
  .social {
    display: flex; align-items: center; gap: 10px;
    color: var(--band-text);
    font-size: 14px;
  }
  .social-mark {
    width: 24px; height: 24px;
    border: 1.5px solid var(--band-text);
    border-radius: 4px;
  }

  .card--back .brand {
    position: absolute; right: 36px; top: 34px;
    text-align: right;
  }
  .card--back .brand-name { font-size: 24px; letter-spacing: 2px; text-align: right; }
  .card--back .brand-tagline { font-size: 11px; letter-spacing: 4px; margin-top: 6px; }

  .person { position: absolute; left: 40px; top: 128px; }
  .person-name { font-family: "Roboto", sans-serif; font-weight: 700; font-size: 21px; }
  .person-role { font-size: 15px; color: var(--muted); margin-top: 2px; }

  .contacts {
    position: absolute; left: 40px; top: 192px;
    list-style: none;
  }
  .contacts li {
    display: flex; align-items: center; gap: 14px;
    font-size: 13.5px; color: var(--muted);
    height: 21px;
  }
  .contacts svg { width: 14px; height: 14px; fill: var(--accent); flex: none; }

  .back-band {
    position: absolute; left: 0; right: 0; bottom: 0;
    height: 24px; background: var(--band);
  }
</style>
</head>
<body>
  <section class="card card--front" aria-label="Business card front">
    <div class="brand">
      <div class="brand-name">VELVET EVENINGS</div>
      <div class="brand-tagline">&amp; Feasts Dubai</div>
    </div>
    <div class="social-band">
      <div class="social"><span class="social-mark"></span>/velveteveningsandfeastsdubai</div>
      <div class="social"><span class="social-mark"></span>/velvetevenings_feasts_dubai/</div>
    </div>
  </section>

  <section class="card card--back" aria-label="Business card back">
    <div class="brand">
      <div class="brand-name">VELVET EVENINGS</div>
      <div class="brand-tagline">&amp; Feasts Dubai</div>
    </div>
    <div class="person">
      <div class="person-name">Gustav ter Brolle</div>
      <div class="person-role">Founder</div>
    </div>
    <ul class="contacts">
      <li>
        <svg viewBox="0 0 16 16" aria-hidden="true"><path d="M3 1.5l3 .5 1 3.5-2 1.2a9 9 0 0 0 4.3 4.3l1.2-2 3.5 1 .5 3c0 .6-.5 1-1 1A13 13 0 0 1 2 2.5c0-.5.4-1 1-1z"/></svg>
        +971 (0)50 - 314 2087
      </li>
      <li>
        <svg viewBox="0 0 16 16" aria-hidden="true"><path d="M1 3h14v10H1z M2 4l6 5 6-5" fill="none" stroke="#e3222b" stroke-width="1.6"/></svg>
        gustav@VvelvetEveningsandFeastsDubai.example
      </li>
      <li>
        <svg viewBox="0 0 16 16" aria-hidden="true"><path d="M1 2h14v9H1z M3 4v5h10V4z M6 12h4v1.5h2V15H4v-1.5h2z" fill-rule="evenodd"/></svg>
        VelvetEveningsandFeastsDubai.example
      </li>
      <li>
        <svg viewBox="0 0 16 16" aria-hidden="true"><path d="M8 1a5 5 0 0 1 5 5c0 4-5 9-5 9S3 10 3 6a5 5 0 0 1 5-5zm0 3a2 2 0 1 0 0 4 2 2 0 0 0 0-4z" fill-rule="evenodd"/></svg>
        P.O. Box 487260, Dubai, UAE
      </li>
    </ul>
    <div class="back-band"></div>
  </section>
</body>
</html>
```